Low Meadow Guild Echoes EP Design Cover

I need a CD cover design for my EP titled "Echoes". The theme can be either the alphabetic letters, or written letters, whichever seems best for your graphic concept.<br/><br/>Please take a listen to the tracks on tunebarn here:<br/>https://tunebarn.example/low-meadow-guild<br/>And here:<br/>https://tunebarn.example/low-meadow-guild/neon-summer/s-QXrT7<br/>https://tunebarn.example/low-meadow-guild/where-did-you-go-draft-mix/s-LKm4P<br/><br/>I look forward to seeing you designs and choosing one for the EP cover.

Target Market(s)

Indie-pop/rock

Colors

Designer to choose colors to be used in the design.

Requirements
Must have
• Low Meadow Guild Logo
• Should meet Chatterbox criteria for % text to picture ratio

```html
<!DOCTYPE html>
<html lang="en">
<head>
<meta charset="utf-8">
<title>Low Meadow Guild — Echoes</title>
<link rel="stylesheet" href="https://fonts.googleapis.com/css2?family=Antonio:wght@300;400&display=swap">
<style>
  :root {
    --paper-light: #a97f71;
    --paper-mid: #8a5e51;
    --paper-dark: #4f2f27;
    --accent-red: #b5121b;
    --mark-white: #f5f1ef;
  }
  html, body {
    margin: 0;
    padding: 0;
    width: 1200px;
    height: 1200px;
    overflow: hidden;
  }
  .cover {
    position: relative;
    width: 1200px;
    height: 1200px;
    overflow: hidden;
  }
  .paper-texture {
    position: absolute;
    inset: 0;
    background:
      radial-gradient(ellipse 70% 60% at 48% 45%, var(--paper-light) 0%, var(--paper-mid) 55%, var(--paper-dark) 100%);
  }
  .wordmark {
    position: absolute;
    inset: 0;
    width: 1200px;
    height: 1200px;
  }
  .wordmark text {
    font-family: "Antonio", "Arial Narrow", sans-serif;
    font-weight: 300;
    text-transform: uppercase;
  }
  .title-vertical {
    fill: var(--accent-red);
  }
  .band-name {
    fill: var(--mark-white);
  }
</style>
</head>
<body>
  <main class="cover">
    <div class="paper-texture" role="img" aria-label="Crumpled brown paper texture with faint diagonal rows of alphabet letters"></div>

    <svg class="wordmark" viewBox="0 0 1200 1200" xmlns="http://www.w3.org/2000/svg" aria-label="Low Meadow Guild — Echoes">
      <g transform="translate(778 1100) rotate(-90)">
        <text class="title-vertical" x="0" y="0" font-size="100" textLength="441" lengthAdjust="spacingAndGlyphs">Echoes</text>
      </g>
      <text class="band-name" x="816" y="812" font-size="186" textLength="281" lengthAdjust="spacing">Low</text>
      <text class="band-name" x="816" y="978" font-size="175" textLength="281" lengthAdjust="spacingAndGlyphs">Meadow</text>
      <text class="band-name" x="816" y="1097" font-size="123" textLength="285" lengthAdjust="spacing">Guild</text>
    </svg>
  </main>
</body>
</html>
```